Business cards for property management company

Need new business cards designed for our property management company and rental community, Blue Fern Commons. These cards will be primarily picked up by rental applicants.

May be single or double sided design.

I need cards for two different people, listed below. The design can be the same for both, and the only information that will be different is name and email address.

Industry/Entity Type

Property Management

Requirements
Must have
• US standard business card - 2''x3.5'' horizontal design.

1. Logo (attached). The text does not have to stay below the logo, but the card does need to say "Blue Fern Commons" somewhere on it (does not have to be same font as logo, but those fonts are Americana Extra Bold and BlackJack if needed).
2. Name: one with "Paula Whitcombe" and one with "Darrell Whitcombe"
3. Email address: one with "paula@bluefernhome.com" and one with "darrell@bluefernhome.com"
4. Web address: bluefernhome.com
5. Phone: 281.604.2218
6. Address: 1783 Wexford Lane, Porterfield, Texas 77812 (zip code may me omitted, at your discretion)
Should not have
• No rounded corners or special cuts.

No bevel, emboss or shadow effects.

As a note, please do not use our website as a basis for color or design schemes. We are working on a redesign, based around the new logo (attached to brief).

```html
<!DOCTYPE html>
<html lang="en">
<head>
<meta charset="utf-8">
<title>Blue Fern Commons – Business Cards</title>
<link rel="stylesheet" href="https://fonts.googleapis.com/css2?family=Arimo:wght@400;700&display=swap">
<style>
  :root {
    --backdrop: #e4e4e2;
    --card-white: #ffffff;
    --panel-green: #4b7d46;
    --panel-teal: #0a8fa3;
    --brand-green: #3f7a45;
    --brand-tint: #dce9da;
    --text-light: #ffffff;
  }
  * { box-sizing: border-box; margin: 0; padding: 0; }
  html, body {
    width: 1200px;
    height: 456px;
    overflow: hidden;
    background: var(--backdrop);
    font-family: "Arimo", Arial, sans-serif;
  }
  .card-row {
    position: relative;
    width: 1200px;
    height: 456px;
  }
  .business-card {
    position: absolute;
    top: 84px;
    width: 507px;
    height: 291px;
    display: flex;
    background: var(--card-white);
  }
  .business-card--paula { left: 76px; }
  .business-card--darrell { left: 619px; }
  .brand-side {
    position: relative;
    width: 253px;
    height: 100%;
  }
  .brand-mark {
    position: absolute;
    left: 82px;
    top: 38px;
    width: 124px;
    height: 124px;
    border-radius: 50%;
    background: var(--brand-tint);
  }
  .brand-name {
    position: absolute;
    left: 0;
    width: 206px;
    top: 176px;
    text-align: center;
    color: var(--brand-green);
    font-size: 27px;
    line-height: 29px;
    font-weight: 700;
  }
  .contact-panel {
    flex: 1;
    height: 100%;
    color: var(--text-light);
    padding: 80px 0 0 30px;
  }
  .business-card--paula .contact-panel { background: var(--panel-green); }
  .business-card--darrell .contact-panel { background: var(--panel-teal); }
  .person-name {
    font-size: 22px;
    font-weight: 400;
    margin-bottom: 12px;
  }
  .contact-list { list-style: none; font-size: 14.5px; line-height: 16.5px; }
  .contact-item { display: flex; align-items: flex-start; }
  .contact-icon {
    width: 14px;
    height: 16.5px;
    margin-right: 7px;
    flex: none;
  }
  .contact-icon--blank { visibility: hidden; }
</style>
</head>
<body>
<div class="card-row">

  <article class="business-card business-card--paula">
    <div class="brand-side">
      <span class="brand-mark"></span>
      <div class="brand-name">Blue Fern<br>Commons</div>
    </div>
    <div class="contact-panel">
      <h2 class="person-name">Paula Whitcombe</h2>
      <ul class="contact-list">
        <li class="contact-item">
          <svg class="contact-icon" viewBox="0 0 14 16.5"><rect x="1" y="4" width="12" height="8.5" fill="#fff"/><path d="M1 4 L7 9 L13 4" fill="none" stroke="#4b7d46" stroke-width="1"/></svg>
          <span>1783 Wexford Lane,</span>
        </li>
        <li class="contact-item">
          <svg class="contact-icon contact-icon--blank" viewBox="0 0 14 16.5"></svg>
          <span>Porterfield, Texas 77812</span>
        </li>
        <li class="contact-item">
          <svg class="contact-icon" viewBox="0 0 14 16.5"><path d="M1 6.5 Q7 1.5 13 6.5 L11 8 L9.5 6.5 L4.5 6.5 L3 8 Z" fill="#fff"/><rect x="3" y="8.5" width="8" height="5" rx="1" fill="#fff"/></svg>
          <span>281.604.2218</span>
        </li>
        <li class="contact-item">
          <svg class="contact-icon" viewBox="0 0 14 16.5"><text x="0" y="13" font-size="14" fill="#fff" font-family="Arimo, sans-serif">@</text></svg>
          <span>paula@bluefernhome.com</span>
        </li>
        <li class="contact-item">
          <svg class="contact-icon" viewBox="0 0 14 16.5"><circle cx="7" cy="8.5" r="5" fill="none" stroke="#fff" stroke-width="1.3"/><path d="M2 8.5 H12 M7 3.5 V13.5" stroke="#fff" stroke-width="1"/></svg>
          <span>bluefernhome.com</span>
        </li>
      </ul>
    </div>
  </article>

  <article class="business-card business-card--darrell">
    <div class="brand-side">
      <span class="brand-mark"></span>
      <div class="brand-name">Blue Fern<br>Commons</div>
    </div>
    <div class="contact-panel">
      <h2 class="person-name">Darrell Whitcombe</h2>
      <ul class="contact-list">
        <li class="contact-item">
          <svg class="contact-icon" viewBox="0 0 14 16.5"><rect x="1" y="4" width="12" height="8.5" fill="#fff"/><path d="M1 4 L7 9 L13 4" fill="none" stroke="#0a8fa3" stroke-width="1"/></svg>
          <span>1783 Wexford Lane,</span>
        </li>
        <li class="contact-item">
          <svg class="contact-icon contact-icon--blank" viewBox="0 0 14 16.5"></svg>
          <span>Porterfield, Texas 77812</span>
        </li>
        <li class="contact-item">
          <svg class="contact-icon" viewBox="0 0 14 16.5"><path d="M1 6.5 Q7 1.5 13 6.5 L11 8 L9.5 6.5 L4.5 6.5 L3 8 Z" fill="#fff"/><rect x="3" y="8.5" width="8" height="5" rx="1" fill="#fff"/></svg>
          <span>281.604.2218</span>
        </li>
        <li class="contact-item">
          <svg class="contact-icon" viewBox="0 0 14 16.5"><text x="0" y="13" font-size="14" fill="#fff" font-family="Arimo, sans-serif">@</text></svg>
          <span>darrell@bluefernhome.com</span>
        </li>
        <li class="contact-item">
          <svg class="contact-icon" viewBox="0 0 14 16.5"><circle cx="7" cy="8.5" r="5" fill="none" stroke="#fff" stroke-width="1.3"/><path d="M2 8.5 H12 M7 3.5 V13.5" stroke="#fff" stroke-width="1"/></svg>
          <span>bluefernhome.com</span>
        </li>
      </ul>
    </div>
  </article>

</div>
</body>
</html>
```